Breezy Lanterns Handcrafted Copper Jewelry

I make handcrafted copper bracelets and cuffs.
I need a banner made (2' 1/2" x 10')
I attached the logo (I would like that sketch to be purple)
Company name: Breezy Lanterns (in a "sassy" font)
Tag line: Bring the Breeze
Designer/Creator: Marla Dunsby
481.307.6624
FB: www.facebook.com/breezylanterns.net
shop.breezylanterns.net
I'd like the background to be white. I'm not sure what I'm looking for as far as the look or if I should add any pics of the copper jewelry that I make. I'm totally up for suggestions. I'm very eager to see how creative you can be.
Many thanks.

```html
<!DOCTYPE html>
<html lang="en">
<head>
<meta charset="utf-8">
<title>Breezy Lanterns – Banner Options</title>
<link rel="stylesheet" href="https://fonts.googleapis.com/css2?family=Lobster&family=Courgette&display=swap">
<style>
  :root {
    --sheet: #e6e6e9;
    --paper: #ffffff;
    --purple: #6a3d9e;
    --purple-soft: #d9cdea;
    --purple-pale: #f1ecf7;
    --rule: #c9c9cf;
  }
  * { margin: 0; padding: 0; box-sizing: border-box; }
  html, body { width: 900px; height: 1200px; overflow: hidden; }
  body { background: var(--sheet); position: relative; font-family: "Courgette", cursive; color: var(--purple); }

  .banner {
    position: absolute; left: 45px; width: 810px; height: 240px;
    background: var(--paper);
    box-shadow: 0 1px 3px rgba(0,0,0,.12);
  }
  .banner--one { top: 40px; }
  .banner--two { top: 330px; }
  .banner--three { top: 620px; }
  .banner--four { top: 910px; }

  .figure-sketch {
    position: absolute; left: 22px; top: 22px; width: 86px; height: 196px;
    background: linear-gradient(180deg, var(--purple-pale), var(--purple-soft));
    border-radius: 40px 40px 8px 8px;
  }

  .brand { position: absolute; left: 122px; top: 26px; width: 340px; }
  .brand__maker { font-size: 19px; text-align: center; }
  .brand__name {
    font-family: "Lobster", cursive; font-size: 108px; line-height: .95;
    text-align: center; letter-spacing: 1px;
  }
  .brand__sub {
    font-family: "Lobster", cursive; font-size: 40px; line-height: 1;
    text-align: right; padding-right: 6px;
  }

  .flag {
    position: absolute; background: var(--purple); color: var(--paper);
    font-family: "Courgette", cursive; text-align: center;
    display: flex; align-items: center; justify-content: center;
  }
  .flag--tall {
    left: 486px; top: 0; width: 96px; height: 190px; font-size: 24px; line-height: 1.15;
    clip-path: polygon(0 0, 100% 0, 100% 100%, 50% 84%, 0 100%);
    padding-bottom: 34px;
  }
  .flag--band {
    left: 480px; top: 34px; width: 310px; height: 52px; font-size: 30px;
    clip-path: polygon(0 0, 100% 0, 100% 100%, 0 100%, 7% 50%);
    padding-left: 18px;
  }
  .flag--square {
    left: 484px; top: 24px; width: 100px; height: 100px; font-size: 22px; line-height: 1.1;
    clip-path: polygon(0 0, 100% 0, 100% 100%, 50% 86%, 0 100%);
    padding-bottom: 14px;
  }

  .contact { position: absolute; text-align: center; }
  .contact--stack { left: 596px; top: 34px; width: 200px; font-size: 16px; line-height: 1.9; }
  .contact--stack .contact__bar { width: 60px; height: 5px; background: var(--rule); margin: 0 auto 6px; border-radius: 3px; }
  .contact--stack .contact__phone { font-size: 20px; }
  .contact--stack .contact__network { margin-top: 20px; font-size: 14px; }
  .contact--wide { left: 480px; top: 98px; width: 310px; font-size: 16px; line-height: 1.4; }
  .contact--wide .contact__phone { font-size: 44px; line-height: 1.1; letter-spacing: 1px; }
  .contact--low { left: 480px; top: 140px; width: 310px; font-size: 16px; line-height: 1.6; }
  .contact--low .contact__phone { font-size: 26px; }
</style>
</head>
<body>

  <section class="banner banner--one">
    <div class="figure-sketch" role="img" aria-label="Purple line sketch of a woman in a dress"></div>
    <div class="brand">
      <p class="brand__maker">Designer/Creator - Marla Dunsby</p>
      <p class="brand__name">Breezy</p>
      <p class="brand__sub">lanterns</p>
    </div>
    <div class="flag flag--tall">Bring<br>the<br>Breeze</div>
    <div class="contact contact--stack">
      <div class="contact__bar"></div>
      <p>shop.breezylanterns.net</p>
      <p class="contact__phone">481.307.6624</p>
      <p>breezylanterns.net</p>
      <p class="contact__network">pagebook</p>
    </div>
  </section>

  <section class="banner banner--two">
    <div class="figure-sketch" role="img" aria-label="Purple line sketch of a woman in a dress"></div>
    <div class="brand">
      <p class="brand__maker">Designer/Creator - Marla Dunsby</p>
      <p class="brand__name">Breezy</p>
      <p class="brand__sub">lanterns</p>
    </div>
    <div class="flag flag--band">Bring the Breeze</div>
    <div class="contact contact--wide">
      <p>www.shop.breezylanterns.net</p>
      <p class="contact__phone">481.307.6624</p>
      <p>pagebook/breezylanterns.net</p>
    </div>
  </section>

  <section class="banner banner--three">
    <div class="figure-sketch" role="img" aria-label="Purple line sketch of a woman in a dress"></div>
    <div class="brand">
      <p class="brand__maker">Designer/Creator - Marla Dunsby</p>
      <p class="brand__name">Breezy</p>
      <p class="brand__sub">lanterns</p>
    </div>
    <div class="flag flag--square">Bring<br>the<br>Breeze</div>
    <div class="contact contact--low">
      <p class="contact__phone">481.307.6624</p>
      <p>pagebook/breezylanterns.net</p>
      <p>www.shop.breezylanterns.net</p>
    </div>
  </section>

  <section class="banner banner--four">
    <div class="figure-sketch" role="img" aria-label="Purple line sketch of a woman in a dress"></div>
    <div class="brand">
      <p class="brand__maker">Designer/Creator - Marla Dunsby</p>
      <p class="brand__name">Breezy</p>
      <p class="brand__sub">lanterns</p>
    </div>
    <div class="flag flag--band">Bring the Breeze</div>
    <div class="contact contact--wide">
      <p>www.shop.breezylanterns.net</p>
      <p class="contact__phone">481.307.6624</p>
      <p>pagebook/breezylanterns.net</p>
    </div>
  </section>

</body>
</html>
```